Behavioral Health Booth Backdrop Design

I need a design created for our backdrop as we are purchasing a new curved 10x10 backdrop for our trade shows. We are a behavioral health (mental health and addiction services) agency and want something that catches your eye when walking by. We don't want a lot of "words" or description on it, but more of a catchy look. I have attached some pics that we like the colors of in general (abstract). This doesn't mean that you need to use these specific pics. I have also attached our Logo with our name.

• Eye catchy design and or a picture/photo with our agency name and/or logo on the backdrop. One of the files to be a vector file.

```html
<!DOCTYPE html>
<html lang="en">
<head>
<meta charset="utf-8">
<title>Aspen Hollow – Booth Backdrop</title>
<link href="https://fonts.googleapis.com/css2?family=Bebas+Neue&family=Bodoni+Moda:wght@400&display=swap" rel="stylesheet">
<style>
  :root {
    --canvas-grey: #dcdcdc;
    --panel-white: #ffffff;
    --panel-edge: #8a8a8a;
    --brand-red: #c9412c;
    --headline-red: #c4382b;
    --tagline-red: #b8322f;
    --silhouette: #2a2727;
    --paper: #efefef;
    --name-ink: #2f3a40;
  }
  * { margin: 0; padding: 0; box-sizing: border-box; }
  html, body {
    width: 1192px;
    height: 1200px;
    overflow: hidden;
    background: var(--canvas-grey);
  }
  .backdrop {
    position: absolute;
    left: 45px;
    top: 50px;
    width: 1102px;
    height: 1100px;
    background: var(--panel-white);
    border: 1px solid var(--panel-edge);
  }
  .brand {
    position: absolute;
    top: 0;
    left: 0;
    width: 100%;
    height: 179px;
    display: flex;
    align-items: center;
    justify-content: center;
    gap: 16px;
    padding-top: 8px;
  }
  .brand-mark {
    width: 34px;
    height: 34px;
    border-radius: 50%;
    background: var(--name-ink);
    flex: none;
  }
  .brand-name {
    font-family: "Bebas Neue", sans-serif;
    font-weight: 400;
    font-size: 46px;
    line-height: 1;
    letter-spacing: 2px;
    color: var(--name-ink);
    white-space: nowrap;
  }
  .hero {
    position: absolute;
    top: 179px;
    left: 0;
    width: 100%;
    height: 784px;
    background: var(--brand-red);
  }
  .hero-art {
    position: absolute;
    inset: 0;
    background: linear-gradient(90deg,
      var(--brand-red) 0%,
      var(--brand-red) 12%,
      var(--silhouette) 24%,
      var(--silhouette) 30%,
      var(--paper) 40%,
      var(--panel-white) 50%,
      var(--paper) 60%,
      var(--silhouette) 70%,
      var(--silhouette) 76%,
      var(--brand-red) 88%,
      var(--brand-red) 100%);
  }
  .headline {
    position: absolute;
    left: 0;
    width: 100%;
    top: 174px;
    text-align: center;
    font-family: "Bebas Neue", sans-serif;
    font-weight: 400;
    font-size: 74px;
    line-height: 77px;
    color: var(--headline-red);
    letter-spacing: 0.5px;
  }
  .tagline {
    position: absolute;
    left: 0;
    bottom: 0;
    width: 100%;
    height: 137px;
    display: flex;
    align-items: center;
    justify-content: center;
    font-family: "Bodoni Moda", serif;
    font-weight: 400;
    font-size: 57px;
    letter-spacing: 2px;
    color: var(--tagline-red);
    padding-bottom: 34px;
  }
</style>
</head>
<body>
  <main class="backdrop">
    <header class="brand">
      <span class="brand-mark"></span>
      <span class="brand-name">Aspen Hollow Behavioral Health</span>
    </header>

    <section class="hero">
      <div class="hero-art" role="img" aria-label="Two dark head silhouettes in profile facing away from each other on a red field, separated by a torn strip of white paper"></div>
      <h1 class="headline">Comprehensive<br>Mental Health<br>and<br>Addiction<br>Services.</h1>
    </section>

    <p class="tagline">WHERE HOPE BEGINS.</p>
  </main>
</body>
</html>
```